Property Investment eBook Cover

I am a long established Australian property investment adviser, analyst and consultant who is now in semi-retired mode and have re-branded to reflect a more casual and personal approach to advising my property investor clients. I am writing a 'revised edition' to a book written in partnership with my father 20 years ago and need an eBook Cover for this new edition. The eBook will be uploaded to all the regular Australian providers (Tarvo Reader, Quillet Epage, Zeni, Pagemarsh)

The 3 key elements in the book cover are:

Title: The Riches Engine of Land. The word 'Property' should be larger and more prominent. eg "The Wealth Power of" could be 1/3 the size of "Property" - with both justified left

Edition: Sydney 2021. "Sydney 2021" should be the focus and dominant imagery of the eBook cover and more prominent than the Title or Author

Author: Glen Markby, The Housing Numbers Guide. The word "Author" should not appear. "The Housing Numbers Guide" should appear underneath Glen Markby and justified to Glen Markby, therefore a smaller font.

The cover should be simple, but eye-catching. No property images, more of an abstract background, than a background with an image. Our preferred colour palette is more blues/greens. Prefer SerifFonts

Copy of book published 20 years ago attached for reference only

```html
<!DOCTYPE html>
<html lang="en">
<head>
<meta charset="utf-8">
<title>The Riches Engine of Land — Sydney 2021</title>
<link rel="stylesheet" href="https://fonts.googleapis.com/css2?family=Cormorant+Garamond:wght@600;700&family=Roboto+Condensed:wght@400;700&display=swap">
<style>
  :root {
    --page-bg: #cfcfcf;
    --teal-light: #5fd6cc;
    --teal-mid: #3bbfb6;
    --teal-deep: #1f8f8a;
    --green-deep: #2f8a5c;
    --green-light: #5cc99a;
    --ink: #0d1a18;
    --band: rgba(12, 26, 24, 0.94);
    --frame: #ffffff;
    --white: #ffffff;
  }
  * { margin: 0; padding: 0; box-sizing: border-box; }
  html, body {
    width: 1200px;
    height: 1200px;
    overflow: hidden;
    background: var(--page-bg);
  }
  .cover {
    position: absolute;
    left: 224px;
    top: 50px;
    width: 752px;
    height: 1100px;
    overflow: hidden;
  }
  .cover-background {
    position: absolute;
    inset: 0;
    background:
      radial-gradient(ellipse at 15% 55%, rgba(20, 110, 100, 0.55), transparent 45%),
      radial-gradient(ellipse at 95% 70%, rgba(30, 120, 70, 0.6), transparent 40%),
      radial-gradient(ellipse at 60% 30%, rgba(110, 230, 220, 0.35), transparent 50%),
      linear-gradient(180deg, var(--teal-mid) 0%, var(--teal-light) 35%, var(--teal-mid) 60%, var(--green-deep) 82%, var(--green-light) 100%);
  }
  .title-frame {
    position: absolute;
    left: 83px;
    top: 83px;
    width: 584px;
    height: 570px;
    border: 2px solid var(--frame);
  }
  .title-line {
    position: absolute;
    font-family: "Cormorant Garamond", Georgia, serif;
    font-weight: 700;
    color: var(--ink);
    line-height: 1;
    white-space: nowrap;
    font-variant: small-caps;
  }
  .title-the    { left: 136px; top: 150px; font-size: 64px; font-variant: normal; }
  .title-riches { left: 154px; top: 233px; font-size: 78px; }
  .title-engine { left: 181px; top: 325px; font-size: 78px; }
  .title-of     { left: 280px; top: 427px; font-size: 62px; font-variant: normal; }
  .title-land   { left: 154px; top: 505px; font-size: 108px; letter-spacing: 1px; }
  .edition-band {
    position: absolute;
    left: 0;
    top: 738px;
    width: 100%;
    height: 132px;
    background: var(--band);
    display: flex;
    align-items: center;
    justify-content: center;
  }
  .edition-text {
    font-family: "Cormorant Garamond", Georgia, serif;
    font-weight: 700;
    font-variant: small-caps;
    font-size: 80px;
    color: var(--white);
    letter-spacing: 1px;
    line-height: 1;
    margin-top: -6px;
  }
  .author-block {
    position: absolute;
    left: 0;
    top: 945px;
    width: 100%;
    text-align: center;
  }
  .author-inner {
    display: inline-block;
    text-align: left;
    font-family: "Roboto Condensed", "Arial Narrow", sans-serif;
    color: var(--ink);
  }
  .author-name {
    font-weight: 700;
    font-size: 31px;
    letter-spacing: 1.5px;
    text-transform: uppercase;
    line-height: 1.05;
  }
  .author-role {
    font-weight: 400;
    font-size: 22px;
    line-height: 1.1;
  }
</style>
</head>
<body>
  <main class="cover">
    <div class="cover-background" role="img" aria-label="Abstract teal and green marbled stone texture background"></div>
    <div class="title-frame"></div>
    <h1 class="book-title">
      <span class="title-line title-the">The</span>
      <span class="title-line title-riches">Riches</span>
      <span class="title-line title-engine">Engine</span>
      <span class="title-line title-of">of</span>
      <span class="title-line title-land">Land</span>
    </h1>
    <div class="edition-band">
      <p class="edition-text">Sydney 2021</p>
    </div>
    <div class="author-block">
      <div class="author-inner">
        <p class="author-name">Glen Markby</p>
        <p class="author-role">The Housing Numbers Guide</p>
      </div>
    </div>
  </main>
</body>
</html>
```